Business Card Design for Flood Rescue 360 - Property Restoration Professionals

I need a business card designed for Flood Rescue 360. We are a full-service property restoration solution. Providing water, fire, smoke & storm restoration as well as mold remediation and full remodel or reconstruction to homes and businesses across Dallas-Fort Worth, TX.
Target Market(s)
home and business owners with insurance covered property damage from water, fire or storm related damage
Industry/Entity Type
property restoration
Contact Information for Business Card
Marcus Pellow General Manager Cell: 214-555-0193 Office: 469-555-0148 email: Marcus@FloodRescue360.example services: Water, Fire, Mold, Reconstruction Tagline: Urgency for Your Water Emergency!
Look and feel
Each slider illustrates characteristics of the customer's brand and the style your logo design should communicate.

```html
<!DOCTYPE html>
<html lang="en">
<head>
<meta charset="utf-8">
<title>Flood Rescue 360 – Business Card</title>
<link rel="stylesheet" href="https://fonts.googleapis.com/css2?family=Roboto:wght@400;500;700;900&display=swap">
<style>
  :root {
    --stage: #d2d3d5;
    --card: #ffffff;
    --brand-blue: #00b2e3;
    --ink-grey: #6d6e71;
    --drop-tone-a: #ffffff;
    --drop-tone-b: #eef0f2;
  }
  html, body {
    margin: 0;
    padding: 0;
    width: 900px;
    height: 1200px;
    overflow: hidden;
    background: var(--stage);
    font-family: "Roboto", Arial, sans-serif;
  }
  .card {
    position: absolute;
    left: 133px;
    width: 632px;
    height: 364px;
    background: var(--card);
    overflow: hidden;
  }
  .card--front { top: 210px; }
  .card--back { top: 624px; }
  .card__texture {
    position: absolute;
    inset: 0;
    background: radial-gradient(ellipse at 50% 50%, var(--drop-tone-a) 0%, var(--drop-tone-b) 100%);
  }
  .brand-name {
    position: absolute;
    margin: 0;
    color: var(--brand-blue);
    font-weight: 900;
    line-height: 0.92;
    text-transform: uppercase;
    letter-spacing: -0.5px;
  }
  .card--front .brand-name {
    left: 103px;
    top: 118px;
    font-size: 66px;
  }
  .tagline {
    position: absolute;
    left: 0;
    right: 0;
    top: 312px;
    margin: 0;
    text-align: center;
    color: var(--ink-grey);
    font-weight: 700;
    font-size: 17px;
    letter-spacing: 1.6px;
    text-transform: uppercase;
  }
  .card--back .brand-name {
    left: 55px;
    top: 146px;
    font-size: 38px;
  }
  .divider {
    position: absolute;
    left: 317px;
    top: 103px;
    width: 2px;
    height: 154px;
    background: var(--ink-grey);
  }
  .contact {
    position: absolute;
    left: 336px;
    top: 100px;
  }
  .contact__name {
    margin: 0;
    color: var(--brand-blue);
    font-weight: 500;
    font-size: 24px;
    letter-spacing: 0.5px;
    text-transform: uppercase;
  }
  .contact__role {
    margin: 4px 0 16px;
    color: var(--ink-grey);
    font-size: 14px;
  }
  .contact__list {
    list-style: none;
    margin: 0;
    padding: 0;
  }
  .contact__item {
    display: flex;
    align-items: center;
    height: 24.5px;
    color: var(--ink-grey);
    font-size: 14.5px;
    font-weight: 500;
  }
  .contact__item--phone { letter-spacing: 2px; }
  .contact__item svg {
    width: 15px;
    height: 15px;
    margin-right: 6px;
    flex: none;
    fill: var(--brand-blue);
  }
  .services {
    position: absolute;
    left: 0;
    right: 0;
    top: 307px;
    margin: 0;
    text-align: center;
    color: var(--ink-grey);
    font-size: 16px;
    font-weight: 500;
  }
  .services__label,
  .services__sep { color: var(--brand-blue); }
</style>
</head>
<body>

<section class="card card--front">
  <div class="card__texture" role="img" aria-label="Background of clear water droplets on white"></div>
  <h1 class="brand-name">Flood<br>Rescue 360</h1>
  <p class="tagline">Urgency for your water emergency!</p>
</section>

<section class="card card--back">
  <div class="card__texture" role="img" aria-label="Background of clear water droplets on white"></div>
  <p class="brand-name">Flood<br>Rescue 360</p>
  <div class="divider"></div>
  <div class="contact">
    <h2 class="contact__name">Marcus Pellow</h2>
    <p class="contact__role">General Manager</p>
    <ul class="contact__list">
      <li class="contact__item contact__item--phone">
        <svg viewBox="0 0 24 24" aria-hidden="true"><path d="M6.6 10.8a15.1 15.1 0 0 0 6.6 6.6l2.2-2.2a1 1 0 0 1 1-.25 11.4 11.4 0 0 0 3.6.57 1 1 0 0 1 1 1V20a1 1 0 0 1-1 1A17 17 0 0 1 3 4a1 1 0 0 1 1-1h3.5a1 1 0 0 1 1 1c0 1.25.2 2.45.57 3.57a1 1 0 0 1-.25 1z"/></svg>
        469-555-0148
      </li>
      <li class="contact__item contact__item--phone">
        <svg viewBox="0 0 24 24" aria-hidden="true"><path d="M8 1h8a2 2 0 0 1 2 2v18a2 2 0 0 1-2 2H8a2 2 0 0 1-2-2V3a2 2 0 0 1 2-2zm0 3v15h8V4zm4 16.2a.9.9 0 1 0 0 1.8.9.9 0 0 0 0-1.8z"/></svg>
        214-555-0193
      </li>
      <li class="contact__item">
        <svg viewBox="0 0 24 24" aria-hidden="true"><path d="M2 5h20v14H2zm2 2v.4l8 5.2 8-5.2V7zm0 2.8V17h16V9.8l-8 5.2z"/></svg>
        Marcus@FloodRescue360.example
      </li>
      <li class="contact__item">
        <svg viewBox="0 0 24 24" aria-hidden="true"><path d="M12 2a10 10 0 1 0 0 20 10 10 0 0 0 0-20zm6.9 9h-3a15.6 15.6 0 0 0-1.3-6.1A8 8 0 0 1 18.9 11zM12 4.1c.9 1.3 1.8 3.7 1.9 6.9h-3.8c.1-3.2 1-5.6 1.9-6.9zM9.4 4.9A15.6 15.6 0 0 0 8.1 11h-3a8 8 0 0 1 4.3-6.1zM5.1 13h3a15.6 15.6 0 0 0 1.3 6.1A8 8 0 0 1 5.1 13zm6.9 6.9c-.9-1.3-1.8-3.7-1.9-6.9h3.8c-.1 3.2-1 5.6-1.9 6.9zm2.6-.8a15.6 15.6 0 0 0 1.3-6.1h3a8 8 0 0 1-4.3 6.1z"/></svg>
        www.FloodRescue360.example
      </li>
    </ul>
  </div>
  <p class="services">
    <span class="services__label">Our Services:</span> Water <span class="services__sep">|</span> Fire <span class="services__sep">|</span> Mold <span class="services__sep">|</span> Reconstruction
  </p>
</section>

</body>
</html>
```